brightpathPRESS is publishing a new book and needs some exceptional cover and layout design!

We are publishing a narrow niche PDF eBook and need both a great cover AND great magazine style layout.

The eBook is a compilation of interviews with 12 financial experts on a particular topic. So the format is is the same for each interview 'chapter'

We are looking for a good front cover/document design that will make what is a pretty dry topic, exciting, interesting and easy to read. Basically - magazine style layout.

The specs for the front cover are:

Title:

The Hurdles and Openings Before Bookkeepers and Planners In Expanding Their Pension Practice In 2014 -2015

by Tom Pelliwick

published by brightpathPRESS

The client would like a similar cover to the one I have attached for your reference. (book front cover example). By no means be limited by this design suggestion. The only caveat is that shots of all interview subjects are included (except the author). These have been included in the zip file.

The design for the text should be elegant and consistent with the design of the front cover. Please format the text in pages 1 to 15 to demonstrate you've understood the brief.

Attached files.

1) MS word version of draft book pages 1 to 15
2) copy of the cover my client would like to emulate.

reminder - this is destined to be a PDF eBook - so looking for some nice eye catching magazine style layout in the design. Columns would be fine.

Good luck!

Brent Malloy
brightpathPRESS

Target Market(s)

Professional Accountants who are running there own businesses

Industry/Entity Type

Financial

Colors

Designer to choose colors to be used in the design.

Requirements
Must have
• The cover must feature headshots of all the interview subjects. The PDF layout must be optimised for viewing on an iPad

```html
<!DOCTYPE html>
<html lang="en">
<head>
<meta charset="utf-8">
<title>The Hurdles &amp; Openings before Bookkeepers &amp; Planners – Tom Pelliwick</title>
<link rel="stylesheet" href="https://fonts.googleapis.com/css2?family=Marcellus&family=Alegreya:wght@800&family=PT+Sans:wght@700&family=Libre+Baskerville:wght@400;700&display=swap">
<style>
  :root {
    --navy: #232a5c;
    --navy-deep: #1e2142;
    --ink: #23234f;
    --orange: #e8502a;
    --byline: #1f7cc0;
    --sky: #8ab4d8;
    --bright: #1a9ad6;
    --mid: #3d6aa8;
    --azure: #3a87c8;
    --slate: #2e3a6a;
    --pale: #d6e4f2;
    --photo: #8d97a6;
    --white: #ffffff;
  }
  * { margin: 0; padding: 0; box-sizing: border-box; }
  html, body { width: 848px; height: 1200px; overflow: hidden; background: var(--white); }
  .cover { position: relative; width: 848px; height: 1200px; overflow: hidden; background: var(--white); }

  .title { position: absolute; left: 0; width: 100%; text-align: center; color: var(--navy); }
  .title-line { position: absolute; left: 0; width: 100%; white-space: nowrap; }
  .title-lead { top: 70px; font-family: "Marcellus", serif; font-size: 38px; }
  .title-lead strong, .title-close strong { font-family: "Alegreya", serif; font-weight: 800; }
  .title-focus { top: 122px; font-family: "PT Sans", sans-serif; font-weight: 700; font-size: 58px; color: var(--orange); letter-spacing: 0.5px; }
  .title-close { top: 192px; font-family: "Marcellus", serif; font-size: 36px; }

  .chart { position: absolute; left: 0; top: 0; }

  .byline { position: absolute; right: 26px; top: 436px; font-family: "Libre Baskerville", serif; font-size: 26px; font-weight: 700; color: var(--byline); }
  .byline span { font-weight: 400; }

  .bar { position: absolute; width: 106px; }
  .bar-tall { left: 106px; top: 388px; height: 114px; background: var(--sky); }
  .bar-mid { left: 212px; top: 445px; height: 57px; background: var(--bright); }

  .grid { position: absolute; left: 0; top: 502px; width: 848px; height: 538px; display: grid; grid-template-columns: repeat(8, 106px); grid-template-rows: repeat(4, 134.5px); }
  .tile { width: 106px; height: 134.5px; }
  .t-white { background: transparent; }
  .t-sky { background: var(--sky); }
  .t-bright { background: var(--bright); }
  .t-mid { background: var(--mid); }
  .t-azure { background: var(--azure); }
  .t-ink { background: var(--ink); }
  .t-slate { background: var(--slate); }
  .t-pale { background: var(--pale); }
  .headshot { background: linear-gradient(180deg, #a7b0bd 0%, var(--photo) 60%, #5d6677 100%); }

  .imprint { position: absolute; left: 0; top: 1040px; width: 848px; height: 160px; background: var(--navy-deep); color: var(--white); text-align: center; font-family: "Libre Baskerville", serif; }
  .imprint-label { position: absolute; top: 48px; width: 100%; font-size: 20px; }
  .imprint-name { position: absolute; top: 84px; width: 100%; font-size: 31px; font-weight: 700; }
</style>
</head>
<body>
<main class="cover">
  <h1 class="title">
    <span class="title-line title-lead">The <strong>Hurdles</strong> &amp; <strong>Openings</strong> before</span>
    <span class="title-line title-focus">BOOKKEEPERS &amp; PLANNERS</span>
    <span class="title-line title-close">in <strong>Expanding</strong> their <strong>Pension Practice</strong></span>
  </h1>

  <svg class="chart" width="848" height="640" viewBox="0 0 848 640" aria-hidden="true">
    <path d="M 560 585 C 440 565, 290 470, 195 305" fill="none" stroke="var(--navy)" stroke-width="14" stroke-linecap="round"/>
    <polygon points="157,245 222,289 168,323" fill="var(--navy)"/>
  </svg>

  <div class="bar bar-tall"></div>
  <div class="bar bar-mid"></div>

  <p class="byline"><span>By</span> TOM PELLIWICK</p>

  <section class="grid" aria-label="Interview subjects">
    <div class="tile headshot" role="img" aria-label="Headshot of interview subject"></div>
    <div class="tile t-sky"></div>
    <div class="tile t-bright"></div>
    <div class="tile t-mid"></div>
    <div class="tile t-white"></div>
    <div class="tile headshot" role="img" aria-label="Headshot of interview subject"></div>
    <div class="tile headshot" role="img" aria-label="Headshot of interview subject"></div>
    <div class="tile t-pale"></div>

    <div class="tile headshot" role="img" aria-label="Headshot of interview subject"></div>
    <div class="tile t-azure"></div>
    <div class="tile headshot" role="img" aria-label="Headshot of interview subject"></div>
    <div class="tile headshot" role="img" aria-label="Headshot of interview subject"></div>
    <div class="tile t-ink"></div>
    <div class="tile t-slate"></div>
    <div class="tile headshot" role="img" aria-label="Headshot of interview subject"></div>
    <div class="tile headshot" role="img" aria-label="Headshot of interview subject"></div>

    <div class="tile t-mid"></div>
    <div class="tile t-ink"></div>
    <div class="tile headshot" role="img" aria-label="Headshot of interview subject"></div>
    <div class="tile t-azure"></div>
    <div class="tile headshot" role="img" aria-label="Headshot of interview subject"></div>
    <div class="tile headshot" role="img" aria-label="Headshot of interview subject"></div>
    <div class="tile t-pale"></div>
    <div class="tile headshot" role="img" aria-label="Headshot of interview subject"></div>

    <div class="tile t-pale"></div>
    <div class="tile headshot" role="img" aria-label="Headshot of interview subject"></div>
    <div class="tile t-azure"></div>
    <div class="tile headshot" role="img" aria-label="Headshot of interview subject"></div>
    <div class="tile headshot" role="img" aria-label="Headshot of interview subject"></div>
    <div class="tile t-mid"></div>
    <div class="tile headshot" role="img" aria-label="Headshot of interview subject"></div>
    <div class="tile t-ink"></div>
  </section>

  <footer class="imprint">
    <p class="imprint-label">Published by</p>
    <p class="imprint-name">Brightpath Press</p>
  </footer>
</main>
</body>
</html>
```